Modern Catering Company needs Letterhead Design

We need a letterhead design that will make effective use of the corporate logo and color scheme, along with careful typography, helps this letterhead design communicate the brand well. We do have a corporate logo, however feel free to enhance the color scheme with gold and purple. We are serving a very upscale clientele so the letterhead has to reflect elegance, professionalism, cleanliness, and modern style. We are branding the company so the letterhead and business cards must fit the brand story. There should be no cartoonish elements in the design and we are looking for sharper lines.

Target Market(s)

Businesses and upscale clientele

Industry/Entity Type

Catering

Contact Information for Business Card

while this design can have any number of quirks and distinctions, it needs to be cohesive with the entire brand story clean, professional but edgy

Requirements
Must have
• must have good and carefully placement of it’s logo and where you place the text or the message. Colors blue, very deep purple, jewel tones not pastels, gold. Blue must be the primary color you may accent with purple or gold. Contact information is as follows: Co-Owners/ Chefs: R. Hollowmere & L. Brandt, phone: 414-555-0182 email:Contact@orchardtablecatering.example, address: 6127 W Larkspur Hollow Rd, Milwaukee, WI 53299
Should not have
• pastel colors, Do not add the BBQ information to the letterhead or business card it was a mistake by the previous designer.

```html
<!DOCTYPE html>
<html lang="en">
<head>
<meta charset="utf-8">
<title>Orchard Table Catering – Letterhead</title>
<link href="https://fonts.googleapis.com/css2?family=Open+Sans:wght@400;600&display=swap" rel="stylesheet">
<style>
  :root {
    --backdrop: #e4e4e4;
    --paper: #ffffff;
    --brand-blue: #2f5fb3;
    --ink: #1c1c1c;
    --frame-grey: #c9c9c9;
    --muted: #444;
  }
  * { box-sizing: border-box; margin: 0; padding: 0; }
  html, body { width: 1200px; height: 1015px; overflow: hidden; }
  body {
    background: var(--backdrop);
    font-family: "Open Sans", Arial, sans-serif;
    color: var(--ink);
  }
  .letterhead {
    position: absolute;
    left: 229px; top: 27px;
    width: 742px; height: 960px;
    background: var(--paper);
    box-shadow: 0 4px 18px rgba(0,0,0,.18);
  }
  .cutlery-border {
    position: absolute;
    inset: 30px;
    border: 6px solid var(--frame-grey);
    border-radius: 2px;
  }
  .brand {
    position: absolute;
    top: 62px; left: 0; right: 0;
    display: flex; flex-direction: column; align-items: center; gap: 10px;
  }
  .brand-mark {
    width: 22px; height: 22px; border-radius: 50%;
    background: var(--brand-blue);
  }
  .brand-name {
    font-size: 24px; font-weight: 400; letter-spacing: 3px;
    color: var(--brand-blue); text-transform: uppercase;
  }
  .letter-body {
    position: absolute;
    top: 240px; left: 88px; right: 88px;
    font-size: 11.5px; line-height: 17px;
  }
  .letter-body p { margin-bottom: 17px; }
  .letter-body p:last-child { margin-bottom: 0; }
  .signature {
    position: absolute;
    left: 100px; top: 690px;
    width: 150px; height: 80px;
    background: linear-gradient(135deg, #f2f2f2, #e2e2e2);
    border-radius: 4px;
  }
  .contact {
    position: absolute;
    bottom: 58px; left: 0; right: 0;
    display: flex; flex-direction: column; align-items: center; gap: 5px;
    font-size: 10px; color: var(--muted); letter-spacing: .3px;
  }
  .contact-row { display: flex; gap: 18px; align-items: center; }
  .contact-item { display: flex; align-items: center; gap: 5px; }
  .contact-item svg { width: 11px; height: 11px; }
  .address { text-transform: uppercase; }
</style>
</head>
<body>
  <main class="letterhead">
    <div class="cutlery-border" role="img" aria-label="Border of small fork and knife icons around the page"></div>

    <header class="brand">
      <span class="brand-mark"></span>
      <span class="brand-name">Orchard Table Catering</span>
    </header>

    <section class="letter-body">
      <p>Lorem Ipsum is simply dummy text of the printing and typesetting industry. Lorem Ipsum has been the industry's standard dummy text ever since the 1500s, when an unknown printer took a galley of type and scrambled it to make a type specimen book. It has survived not only five centuries, but also the leap into electronic typesetting, remaining essentially unchanged. It was popularised in the 1960s with the release of Typeline sheets containing Lorem Ipsum passages, and more recently with desktop publishing software like Quillset Layout including versions of Lorem Ipsum.</p>
      <p>It is a long established fact that a reader will be distracted by the readable content of a page when looking at its layout. The point of using Lorem Ipsum is that it has a more-or-less normal distribution of letters, as opposed to using 'Content here, content here', making it look like readable English. Many desktop publishing packages and web page editors now use Lorem Ipsum as their default model text, and a search for 'lorem ipsum' will uncover many web sites still in their infancy. Various versions have evolved over the years, sometimes by accident, sometimes on purpose (injected humour and the like).</p>
      <p>Contrary to popular belief, Lorem Ipsum is not simply random text. It has roots in a piece of classical Latin literature from 45 BC, making it over 2000 years old. Harold Brenwick, a Latin professor at Ashgrove College, looked up one of the more obscure Latin words, consectetur, from a Lorem Ipsum passage, and going through the cites of the word in classical literature, discovered the undoubtable source. Lorem Ipsum comes from sections 1.10.32 and 1.10.33 of "de Ordine Mensae" (The Order of the Table) by Varinus Sollo, written in 45 BC. This book is a treatise on the theory of ethics, very popular during the Renaissance. The first line of Lorem Ipsum, "Lorem ipsum dolor sit amet..", comes from a line in section 1.10.32.</p>
    </section>

    <div class="signature" role="img" aria-label="Handwritten signature"></div>

    <footer class="contact">
      <div class="contact-item">
        <svg viewBox="0 0 12 12"><circle cx="6" cy="6" r="6" fill="var(--brand-blue)"/><rect x="3" y="4" width="6" height="4" fill="none" stroke="#fff" stroke-width="1"/><path d="M3 4l3 2.2L9 4" fill="none" stroke="#fff" stroke-width="1"/></svg>
        <span>Contact@orchardtablecatering.example</span>
      </div>
      <div class="contact-row">
        <div class="contact-item">
          <svg viewBox="0 0 12 12"><circle cx="6" cy="6" r="6" fill="var(--brand-blue)"/><path d="M4 3.2l1.2 1.4-.6.8a4 4 0 0 0 2 2l.8-.6 1.4 1.2-.8 1A5 5 0 0 1 3 4z" fill="#fff"/></svg>
          <span>414-555-0182</span>
        </div>
        <div class="contact-item">
          <svg viewBox="0 0 12 12"><circle cx="6" cy="6" r="6" fill="var(--brand-blue)"/><rect x="3.5" y="3" width="5" height="6" fill="#fff"/></svg>
          <span>414-555-0147</span>
        </div>
      </div>
      <div class="address">6127 W Larkspur Hollow Rd, Milwaukee, WI 53299</div>
    </footer>
  </main>
</body>
</html>
```